Mini Market Tavo Business Presentation Cards

We need presentation cards with a logo we already own designed at this website as well. We need the printing, delivery and sleek, modem design in harmony with our previous logo design.

Target Market(s)

Low, med and High income class.

Industry/Entity Type

Grocery Store

Contact Information for Business Card

Business logo (Mini Market Tavo), name: Esteban L. Morales/Lidia M. Paz/ Hugo Paz (those are the names for the different cards),
Address: Col. Lomas del Viento, carretera a Tela a 200mts del Centro Comunal. Puerto Cortés, Honduras.
Email: minimarkettavo@correo-ejemplo.hn
Teléfono: (504) 9731-5064

Font styles to use
Serif
Sans Serif

Requirements
Must have
• Business logo (Mini Market Tavo), person name, department,
• Address, phone number, email address.

```html
<!DOCTYPE html>
<html lang="es">
<head>
<meta charset="utf-8">
<title>Mini Market Tavo – Tarjeta de presentación</title>
<link href="https://fonts.googleapis.com/css2?family=Noto+Sans:wght@400&family=Noto+Serif:wght@400;700&display=swap" rel="stylesheet">
<style>
  :root {
    --backdrop: #e9e6e1;
    --card: #f7f7f6;
    --brand-red: #e04a35;
    --brand-green: #79b54f;
    --rule-green: #8cc063;
    --ink: #2a2a2a;
    --ink-soft: #3a3a3a;
  }
  html, body {
    margin: 0;
    width: 1200px;
    height: 902px;
    overflow: hidden;
    background: var(--backdrop);
  }
  .business-card {
    position: absolute;
    left: 100px;
    top: 161px;
    width: 1000px;
    height: 580px;
    background: var(--card);
    box-shadow: 0 6px 24px rgba(0,0,0,0.12);
  }
  .brand {
    position: absolute;
    right: 70px;
    top: 40px;
    display: flex;
    align-items: center;
    gap: 28px;
  }
  .brand-name {
    font-family: "Noto Serif", Georgia, serif;
    font-weight: 400;
    font-size: 52px;
    color: var(--brand-red);
    white-space: nowrap;
  }
  .brand-dot {
    width: 200px;
    height: 200px;
    border-radius: 50%;
    background: var(--brand-green);
  }
  .name-rule {
    position: absolute;
    left: 0;
    right: 0;
    top: 318px;
    height: 40px;
    display: flex;
    align-items: center;
  }
  .name-rule .rule {
    flex: 1;
    height: 3px;
    background: var(--rule-green);
  }
  .name-rule .rule.left { flex: 0 0 220px; }
  .person-name {
    font-family: "Noto Serif", Georgia, serif;
    font-weight: 700;
    font-size: 38px;
    letter-spacing: 2px;
    color: var(--ink);
    padding: 0 22px;
    white-space: nowrap;
  }
  .contact {
    position: absolute;
    left: 0;
    right: 0;
    top: 388px;
    text-align: center;
    font-family: "Noto Sans", Arial, sans-serif;
    font-size: 25px;
    line-height: 1.38;
    color: var(--ink-soft);
    letter-spacing: 1px;
  }
  .contact p { margin: 0; }
</style>
</head>
<body>
  <article class="business-card">
    <header class="brand">
      <span class="brand-name">Mini Market Tavo</span>
      <span class="brand-dot" aria-hidden="true"></span>
    </header>
    <div class="name-rule">
      <span class="rule left"></span>
      <h1 class="person-name" style="margin:0">Esteban L. Morales</h1>
      <span class="rule right"></span>
    </div>
    <address class="contact" style="font-style:normal">
      <p class="phone">(504) 9731-5064</p>
      <p class="email">minimarkettavo@correo-ejemplo.hn</p>
      <p class="street">Col. Lomas del Viento, carretera a Tela a</p>
      <p class="city">200mts del Centro Comunal. Puerto Cortés, Honduras.</p>
    </address>
  </article>
</body>
</html>
```